Christmas Card 2021

We need a design for a Christmas Card in the format DIN A5 (148 x 210 mm). KELTO is an Austrian company with branches all over Europe. KELTO handles international claims for insurance companies. The Christmas Card will be sent to all our clients all over Europe and beyond.
The design must include our logo (see uploaded file). The color blue that we use is: CMYK: 100/16/0/27 or RGB: 0/114/168.
The card must have this text:
Fröhliche Weihnachten und ein gutes neues Jahr!
Merry Christmas and Happy New Year!
Joyeux Noël et bonne année !
Optional you can use our key visual (see uploaded file).
Optional you can use our motto text: worldwide claims service
We are looking forward to your design!
Kind regards
Lukas

```html
<!DOCTYPE html>
<html lang="en">
<head>
<meta charset="utf-8">
<title>KELTO Christmas Card 2021</title>
<link rel="stylesheet" href="https://fonts.googleapis.com/css2?family=Dancing+Script:wght@500&display=swap">
<style>
  :root {
    --card-blue: #0f6fa8;
    --cream: #fbe7da;
    --ornament-soft: rgba(251, 231, 218, 0.22);
    --ornament-fade: rgba(251, 231, 218, 0);
    --bow-red: rgba(232, 68, 76, 0.35);
  }
  * { margin: 0; padding: 0; box-sizing: border-box; }
  html, body {
    width: 886px;
    height: 1200px;
    overflow: hidden;
    background: var(--card-blue);
  }
  .card {
    position: relative;
    width: 886px;
    height: 1200px;
    background: var(--card-blue);
    color: var(--cream);
    font-family: "Dancing Script", cursive;
  }
  .branch {
    position: absolute;
    border-radius: 40px;
  }
  .branch--top-right {
    left: 460px; top: 14px; width: 390px; height: 380px;
    background: radial-gradient(ellipse at 85% 12%, var(--bow-red) 0 12%, var(--ornament-soft) 30%, var(--ornament-fade) 72%);
  }
  .branch--bottom-left {
    left: 22px; top: 782px; width: 420px; height: 410px;
    background: radial-gradient(ellipse at 14% 88%, var(--bow-red) 0 12%, var(--ornament-soft) 30%, var(--ornament-fade) 72%);
  }
  .snowflake {
    position: absolute;
    border-radius: 50%;
    background: radial-gradient(circle, rgba(251, 231, 218, 0.75) 0 30%, rgba(251, 231, 218, 0.25) 60%, var(--ornament-fade) 72%);
  }
  .greetings {
    position: absolute;
    left: 0; right: 0; top: 0;
    text-align: center;
    font-size: 42px;
    font-weight: 500;
    line-height: 1;
  }
  .greeting {
    position: absolute;
    left: 0; right: 0;
  }
  .greeting--de { top: 445px; }
  .greeting--en { top: 572px; }
  .greeting--fr { top: 693px; }
  .brand-name {
    position: absolute;
    left: 0; width: 882px;
    top: 940px;
    text-align: center;
    font-size: 64px;
    font-weight: 500;
    color: var(--cream);
  }
</style>
</head>
<body>
  <main class="card">
    <div class="branch branch--top-right" role="img" aria-label="Winter branch with berries and a red bow in the top right corner"></div>
    <div class="branch branch--bottom-left" role="img" aria-label="Winter branch with berries and a red bow in the bottom left corner"></div>

    <div class="snowflake" role="img" aria-label="Snowflake" style="left:72px; top:57px; width:72px; height:72px;"></div>
    <div class="snowflake" role="img" aria-label="Snowflake" style="left:159px; top:172px; width:32px; height:32px;"></div>
    <div class="snowflake" role="img" aria-label="Snowflake" style="left:56px; top:202px; width:44px; height:44px;"></div>
    <div class="snowflake" role="img" aria-label="Snowflake" style="left:792px; top:954px; width:44px; height:44px;"></div>
    <div class="snowflake" role="img" aria-label="Snowflake" style="left:703px; top:998px; width:28px; height:28px;"></div>
    <div class="snowflake" role="img" aria-label="Snowflake" style="left:750px; top:1071px; width:72px; height:72px;"></div>

    <section class="greetings">
      <p class="greeting greeting--de">Fröhliche Weihnachten und ein gutes neues Jahr!</p>
      <p class="greeting greeting--en">Merry Christmas and Happy New Year!</p>
      <p class="greeting greeting--fr">Joyeux Noël et bonne année!</p>
    </section>

    <p class="brand-name">KELTO</p>
  </main>
</body>
</html>
```